I need a full PowerPoint template (with multiple slide options) for a new imaging center company - Lumora Medical Imaging. I have attached the Logo and Brand Identity here.

```html
<!DOCTYPE html>
<html lang="en">
<head>
<meta charset="utf-8">
<title>Lumora Medical Imaging – Presentation Template</title>
<link href="https://fonts.googleapis.com/css2?family=Montserrat:ital,wght@0,300;0,400;0,500;0,600;0,700;0,800;1,300;1,800&display=swap" rel="stylesheet">
<style>
:root{
  --stage:#7f7f7f;
  --ink:#1b1b3f;
  --navy:#1a1a5c;
  --blue:#0a6fc2;
  --sky:#1e88d6;
  --green:#16a34a;
  --white:#ffffff;
  --dark:#1f2023;
  --text:#2b2b3a;
}
*{box-sizing:border-box;margin:0;padding:0}
html,body{width:1200px;height:789px;overflow:hidden;background:var(--stage);font-family:"Montserrat",sans-serif}
.slide{position:absolute;width:493px;height:277px;background:var(--white);overflow:hidden;box-shadow:0 6px 14px rgba(0,0,0,.35)}
.slide--cover{left:88px;top:103px;background:var(--dark)}
.slide--about{left:619px;top:103px}
.slide--services{left:88px;top:409px}
.slide--commitment{left:619px;top:409px}
.abs{position:absolute}
.photo{position:absolute}
/* cover */
.cover-photo{left:236px;top:0;width:257px;height:277px;background:linear-gradient(200deg,#3f7fb8 0%,#245a8f 40%,#173a5e 75%,#1f2023 100%)}
.cover-fade{left:200px;top:0;width:90px;height:277px;background:linear-gradient(90deg,var(--dark),rgba(31,32,35,0))}
.brand{left:28px;top:36px;display:flex;align-items:center;gap:6px;color:var(--white);font-weight:700}
.brand-dot{width:32px;height:32px;border-radius:50%;background:var(--sky)}
.brand-name{font-size:21px;line-height:1;font-weight:700;letter-spacing:.5px}
.brand-sub{font-size:7.5px;letter-spacing:1px;margin-top:3px;font-weight:700}
.headline{left:28px;top:102px;font-size:21.5px;line-height:24.5px;font-weight:800;font-style:italic;color:var(--white)}
.headline .accent{color:var(--sky);font-style:normal}
.headline .light{font-weight:300}
.cover-rule{left:30px;top:175px;width:176px;height:2px;background:var(--green)}
.cover-sub{left:28px;top:193px;width:300px;font-size:13.4px;line-height:16.5px;font-weight:300;color:#e8e8ee}
.pill{position:absolute;border:1px solid var(--ink);border-radius:12px;font-size:10.5px;font-weight:400;text-align:center;line-height:13px;color:var(--ink)}
.cover-pill{left:355px;top:239px;width:109px;height:15px;font-size:10px;border-color:#cfd3da;color:#e8e8ee;line-height:13px}
/* shared */
.title{position:absolute;font-size:21px;line-height:24px;font-weight:300;color:var(--navy);letter-spacing:.3px}
.title b{font-weight:800}
.rule{position:absolute;height:1.5px;background:var(--green)}
.body{position:absolute;font-size:9.2px;line-height:11px;font-weight:400;color:var(--text)}
.bullets{position:absolute;list-style:none;font-size:9.3px;line-height:13.3px;color:var(--text)}
.bullets li{position:relative;padding-left:9px}
.bullets li::before{content:"";position:absolute;left:0;top:4.5px;width:3.5px;height:3.5px;background:var(--green)}
.band{position:absolute;left:0;top:240px;width:355px;height:19px;background:var(--green);border-radius:0 10px 10px 0;color:var(--white);font-size:9px;font-weight:600;line-height:19px;padding-left:25px;white-space:nowrap}
.band-pill{left:363px;top:241px;width:113px;height:16px;line-height:14px}
.footbar{position:absolute;left:0;bottom:0;width:493px;height:10px;background:linear-gradient(90deg,var(--sky),var(--navy) 60%,#151545)}
/* about */
.about-photo{left:282px;top:0;width:211px;height:130px;border-radius:0 0 0 46px;background:linear-gradient(135deg,#9fd0e6,#4d8fb0 55%,#2b4a66)}
/* services */
.services-photo{left:0;top:0;width:128px;height:206px;border-radius:0 0 40px 0;background:linear-gradient(160deg,#5d90b8,#1f4468 55%,#dfe7ef)}
.svc{position:absolute;display:flex;align-items:center;gap:6px;font-size:9px;font-weight:600;color:var(--ink)}
.svc svg{width:11px;height:11px}
/* commitment */
.commit-panel{left:0;top:0;width:266px;height:206px;border-radius:0 0 22px 0;background:linear-gradient(180deg,var(--navy),var(--blue))}
.commit-title{color:var(--white)}
.why{left:26px;top:92px;width:200px;font-size:12.2px;line-height:15px;font-weight:700;color:var(--white)}
.commit-body{left:26px;top:126px;width:190px;color:#d5e3f5}
.ring{left:279px;top:10px;width:121px;height:121px;border-radius:50%;border:2.5px solid var(--navy);padding:4px}
.ring-photo{width:100%;height:100%;border-radius:50%;background:linear-gradient(135deg,#c9d6e0,#7a8fa3 60%,#3b4d63)}
.core{left:283px;top:139px;font-size:10.5px;font-weight:700;color:var(--green);letter-spacing:.3px}
</style>
</head>
<body>

<section class="slide slide--cover">
  <div class="photo cover-photo" role="img" aria-label="MRI scanner in a dimly lit imaging room"></div>
  <div class="abs cover-fade"></div>
  <div class="abs brand">
    <div class="brand-dot"></div>
    <div><div class="brand-name">LUMORA</div><div class="brand-sub">— MEDICAL IMAGING —</div></div>
  </div>
  <div class="abs headline">PRECISION IMAGING.<br><span class="accent">CLEAR ANSWERS.</span><br><span class="light">TRUSTED CARE.</span></div>
  <div class="abs cover-rule"></div>
  <p class="abs cover-sub">Advanced diagnostic imaging designed for accuracy, comfort, and confidence.</p>
  <div class="pill cover-pill">www.website.com</div>
</section>

<section class="slide slide--about">
  <h2 class="title" style="left:26px;top:40px">WHO <b>WE ARE?</b></h2>
  <div class="rule" style="left:26px;top:65px;width:240px"></div>
  <div class="photo about-photo" role="img" aria-label="Two clinicians reviewing an X-ray film at a workstation"></div>
  <p class="body" style="left:26px;top:86px;width:244px">Lumora Medical Imaging is a modern diagnostic imaging centre dedicated to delivering accurate, reliable, and timely medical imaging services. Our facility combines advanced imaging technology with a patient-focused approach to support clinicians in making confident diagnostic decisions.</p>
  <p class="body" style="left:26px;top:164px;width:240px">We prioritise clinical excellence, operational efficiency, and compassionate care—ensuring every patient receives a seamless and reassuring experience from referral to results.</p>
  <ul class="bullets" style="left:283px;top:160px;width:196px">
    <li>State-of-the-art imaging technology</li>
    <li>Experienced radiographers &amp; specialists</li>
    <li>Fast reporting &amp; reliable diagnostics</li>
    <li style="line-height:10px;padding-top:1.5px">Comfortable, patient-friendly environment</li>
  </ul>
  <div class="band">• MRI • CT • X-Ray • Ultrasound• Patient-First Diagnostic Services</div>
  <div class="pill band-pill">www.website.com</div>
  <div class="footbar"></div>
</section>

<section class="slide slide--services">
  <div class="photo services-photo" role="img" aria-label="Doctor examining a spine X-ray"></div>
  <h2 class="title" style="left:139px;top:46px">OUR <b>SERVICES</b></h2>
  <div class="rule" style="left:139px;top:71px;width:241px"></div>
  <p class="body" style="left:139px;top:92px;width:315px">We offer a full range of medical imaging solutions designed to meet the needs of patients, physicians, and healthcare partners.</p>
  <div class="svc" style="left:138px;top:125px"><svg viewBox="0 0 12 12"><path d="M4 1h4v3h3v4H8v3H4V8H1V4h3z" fill="none" stroke="#16a34a" stroke-width="1"/></svg>Magnetic Resonance Imaging (MRI)</div>
  <div class="svc" style="left:138px;top:144px"><svg viewBox="0 0 12 12"><path d="M4 1h4v3h3v4H8v3H4V8H1V4h3z" fill="none" stroke="#16a34a" stroke-width="1"/></svg>Computed Tomography (CT)</div>
  <div class="svc" style="left:354px;top:125px"><svg viewBox="0 0 12 12"><path d="M4 1h4v3h3v4H8v3H4V8H1V4h3z" fill="none" stroke="#16a34a" stroke-width="1"/></svg>Digital X-Ray</div>
  <div class="svc" style="left:354px;top:144px"><svg viewBox="0 0 12 12"><path d="M4 1h4v3h3v4H8v3H4V8H1V4h3z" fill="none" stroke="#16a34a" stroke-width="1"/></svg>Ultrasound Imaging</div>
  <p class="body" style="left:139px;top:169px;width:266px">Each service is delivered with strict quality standards, advanced equipment, and highly trained professionals to ensure precise results and patient safety.</p>
  <div class="band">• MRI • CT • X-Ray • Ultrasound• Patient-First Diagnostic Services</div>
  <div class="pill band-pill">www.website.com</div>
  <div class="footbar"></div>
</section>

<section class="slide slide--commitment">
  <div class="abs commit-panel"></div>
  <h2 class="title commit-title" style="left:26px;top:46px">OUR <b>COMMITMENT</b></h2>
  <div class="rule" style="left:26px;top:71px;width:220px;background:var(--white)"></div>
  <h3 class="abs why">Why Choose Lumora Medical Imaging?</h3>
  <p class="body commit-body">At Lumora Medical Imaging, our mission is to bring clarity to healthcare decisions through precision imaging and dependable diagnostics.</p>
  <div class="abs ring"><div class="ring-photo" role="img" aria-label="Caregiver and young patient looking at a laptop in a hospital room"></div></div>
  <div class="abs core">CORE COMMITMENTS:</div>
  <ul class="bullets" style="left:283px;top:156px;width:185px">
    <li>Clinical accuracy and consistency</li>
    <li>Patient comfort, privacy, and care</li>
    <li>Efficient scheduling and fast turnaround times</li>
    <li>Collaboration with referring physicians</li>
  </ul>
  <div class="band">• MRI • CT • X-Ray • Ultrasound• Patient-First Diagnostic Services</div>
  <div class="pill band-pill">www.website.com</div>
  <div class="footbar"></div>
</section>

</body>
</html>
```